Boutique Real Estate Brokerage looking for business card, letterhead and envelope design

We are looking for a cohesive design for our business cards, letterhead and envelopes and that mirrors our high-end homes and clientele. Fern & Gable is being launched and designed for the marketplace of tomorrow. We grew from the #1 team in our community into a full-service firm that is going to revolutionize the traditional real estate model.

We understand that it’s more important than ever to help our clients and partners adapt to behavioral and market changes being driven by generational shifts and technological advances in society, and by combining traditional brokerage services with innovative production and marketing capabilities, we know how to do that better than anyone else.

Requirements
Must have
• business card, letterhead and envelope design - attached logo.

```html
<!DOCTYPE html>
<html lang="en">
<head>
<meta charset="utf-8">
<title>Fern &amp; Gable Realty — Stationery</title>
<link rel="stylesheet" href="https://fonts.googleapis.com/css2?family=Lato:ital,wght@0,400;0,700;0,900;1,400&display=swap">
<style>
  :root {
    --navy: #140a4f;
    --gold: #b9803a;
    --paper: #ffffff;
    --ink: #3c3c46;
    --muted: #8a8a94;
    --backdrop: #6aa6a3;
  }
  * { box-sizing: border-box; margin: 0; padding: 0; }
  html, body { width: 1200px; height: 2472px; overflow: hidden; }
  body {
    background: var(--backdrop);
    font-family: "Lato", sans-serif;
    color: var(--ink);
    position: relative;
  }
  .sheet {
    position: absolute;
    background: var(--paper);
    box-shadow: 0 18px 40px rgba(0,0,0,.18);
    overflow: hidden;
  }
  .shape-layer { position: absolute; inset: 0; width: 100%; height: 100%; }

  .wordmark {
    display: flex; align-items: center; gap: 12px;
    font-family: "Lato", sans-serif; font-weight: 900;
    color: var(--navy); letter-spacing: .02em; white-space: nowrap;
  }
  .wordmark .mark-square { background: var(--gold); flex: none; }

  /* Business card back */
  .card-back { left: 70px; top: 180px; width: 500px; height: 290px;
    display: flex; align-items: center; justify-content: center; }
  .card-back .wordmark { font-size: 34px; }
  .card-back .mark-square { width: 30px; height: 30px; }

  /* Business card front */
  .card-front { left: 630px; top: 180px; width: 500px; height: 290px; }
  .card-front .wordmark { position: absolute; left: 34px; top: 38px; font-size: 22px; gap: 10px; }
  .card-front .mark-square { width: 20px; height: 20px; }
  .card-front .person { position: absolute; left: 34px; top: 90px; }
  .person-name { font-weight: 900; font-size: 17px; color: var(--navy); }
  .person-role { font-weight: 700; font-size: 13px; color: var(--gold); margin-top: 2px; }
  .card-front .address { position: absolute; left: 34px; top: 142px; font-size: 11.5px; color: var(--muted);
    display: flex; align-items: center; gap: 7px; }
  .card-front .contacts { position: absolute; left: 34px; top: 204px; color: #fff; font-size: 12px; }
  .contact-line { display: flex; align-items: center; gap: 8px; line-height: 1.7; white-space: nowrap; }
  .icon { width: 11px; height: 11px; flex: none; }

  /* Letterhead */
  .letterhead { left: 280px; top: 600px; width: 640px; height: 905px; }
  .letterhead .wordmark { position: absolute; left: 230px; top: 52px; font-size: 22px; gap: 10px; }
  .letterhead .mark-square { width: 20px; height: 20px; }
  .recipient { position: absolute; left: 60px; top: 120px; font-size: 9px; color: var(--muted); line-height: 1.5; }
  .recipient .to-label { font-size: 8px; }
  .recipient .to-name { font-size: 16px; font-weight: 900; color: var(--navy); }
  .recipient .label { color: var(--gold); font-weight: 700; }
  .letter-date { position: absolute; right: 60px; top: 226px; font-size: 9px; color: var(--muted); font-style: italic; }
  .salutation { position: absolute; left: 60px; top: 250px; font-size: 9px; color: var(--muted); font-style: italic; }
  .letter-body { position: absolute; left: 60px; right: 60px; top: 280px; font-size: 9.5px; line-height: 1.7;
    color: var(--muted); font-style: italic; }
  .letter-body p + p { margin-top: 12px; }
  .letter-body .lead { color: var(--ink); font-weight: 700; }
  .sign-off { position: absolute; left: 60px; top: 470px; }
  .sign-off .person-name { font-size: 13px; font-weight: 700; }
  .sign-off .person-role { font-size: 8px; color: var(--muted); font-weight: 400; }
  .signature-area { width: 120px; height: 34px; margin-top: 8px; background: linear-gradient(90deg, #e4e6f5, #f4f5fb); border-radius: 4px; }
  .letterhead .contacts { position: absolute; left: 40px; bottom: 30px; color: #fff; font-size: 10px;
    display: grid; grid-template-columns: auto auto; column-gap: 28px; }

  /* Envelope */
  .envelope { left: 80px; top: 1680px; width: 1040px; height: 500px; }
  .envelope .wordmark { position: absolute; left: 70px; top: 70px; font-size: 36px; gap: 14px; }
  .envelope .mark-square { width: 32px; height: 32px; }
  .envelope .contacts { position: absolute; left: 70px; top: 250px; font-size: 19px; color: var(--muted); }
  .envelope .contact-line { gap: 14px; line-height: 1.75; }
  .envelope .icon { width: 15px; height: 15px; }
  .address-window { position: absolute; right: 80px; top: 90px; width: 330px; height: 160px; border-radius: 10px;
    background: linear-gradient(120deg, #2a2168 0%, #4a4283 55%, #5b5590 100%); }
</style>
</head>
<body>

<svg width="0" height="0" style="position:absolute">
  <defs>
    <symbol id="i-pin" viewBox="0 0 12 12"><path d="M6 1a3.6 3.6 0 0 0-3.6 3.6C2.4 7.3 6 11 6 11s3.6-3.7 3.6-6.4A3.6 3.6 0 0 0 6 1zm0 5a1.4 1.4 0 1 1 0-2.8A1.4 1.4 0 0 1 6 6z" fill="#b9803a"/></symbol>
    <symbol id="i-phone" viewBox="0 0 12 12"><path d="M3.2 1.2l1.6 2.2-.9 1.2a6.5 6.5 0 0 0 3.5 3.5l1.2-.9 2.2 1.6-.8 1.6C6 10.6 1.4 6 1.6 2z" fill="#b9803a"/></symbol>
    <symbol id="i-mail" viewBox="0 0 12 12"><path d="M1 6.2L11 1 7.4 11 6 7z" fill="#b9803a"/></symbol>
    <symbol id="i-web" viewBox="0 0 12 12"><path d="M5 7l2-2M4.2 5.6L2.8 7a1.6 1.6 0 0 0 2.2 2.2l1.4-1.4M7.8 6.4L9.2 5A1.6 1.6 0 0 0 7 2.8L5.6 4.2" stroke="#b9803a" stroke-width="1.4" fill="none" stroke-linecap="round"/></symbol>
  </defs>
</svg>

<!-- Business card, logo side -->
<section class="sheet card-back">
  <div class="wordmark"><span class="mark-square"></span>Fern &amp; Gable Realty</div>
</section>

<!-- Business card, contact side -->
<section class="sheet card-front">
  <svg class="shape-layer" viewBox="0 0 500 290" preserveAspectRatio="none">
    <path d="M0 290 L0 188 C150 184 310 160 385 122 C418 107 450 104 500 104 L500 290 Z" fill="var(--navy)"/>
    <path d="M405 100 L500 28 L500 96 Z" fill="var(--gold)"/>
  </svg>
  <div class="wordmark"><span class="mark-square"></span>Fern &amp; Gable Realty</div>
  <div class="person">
    <div class="person-name">YOUR FULL NAME</div>
    <div class="person-role">Designation</div>
  </div>
  <div class="address"><svg class="icon"><use href="#i-pin"/></svg>27 Maple Row Eastfield, CT 06000</div>
  <div class="contacts">
    <div class="contact-line"><svg class="icon"><use href="#i-phone"/></svg>(+00) 555 0142 776</div>
    <div class="contact-line"><svg class="icon"><use href="#i-mail"/></svg>info@fernandgablerealty.com</div>
    <div class="contact-line"><svg class="icon"><use href="#i-web"/></svg>www.fernandgablerealty.com</div>
  </div>
</section>

<!-- Letterhead -->
<section class="sheet letterhead">
  <svg class="shape-layer" viewBox="0 0 640 905" preserveAspectRatio="none">
    <path d="M0 905 L0 800 L430 800 C470 800 480 830 490 905 Z" fill="var(--navy)"/>
    <path d="M505 905 L520 830 L640 905 Z" fill="var(--gold)"/>
  </svg>
  <div class="wordmark"><span class="mark-square"></span>Fern &amp; Gable Realty</div>
  <div class="recipient">
    <div class="to-label">TO</div>
    <div class="to-name">Harold</div>
    <div>Designation</div>
    <div><span class="label">Address:</span> 18 Birch Lane, Northport, CT 06010</div>
    <div><span class="label">Email:</span> harold@mailbox.com</div>
    <div><span class="label">Phone:</span> (+00) 555 0188 214</div>
  </div>
  <div class="letter-date">Date: 27.07.2019</div>
  <div class="salutation">Dear Mr. ________</div>
  <div class="letter-body">
    <p>Thank you for meeting with our team this week. We enjoyed walking through the property with you and learning more about what you hope to find in your next home. Below is a short summary of the listings we discussed, along with the next steps we suggested.</p>
    <p class="lead">Each home on the list was chosen for its location, light and layout, and all three are available to view this month.</p>
    <p>Please let us know which times suit you best, and we will arrange private tours. We look forward to helping you settle in.</p>
  </div>
  <div class="sign-off">
    <div class="person-name">Your Name</div>
    <div class="person-role">Designation</div>
    <div class="signature-area" role="img" aria-label="Handwritten signature"></div>
  </div>
  <div class="contacts">
    <div class="contact-line"><svg class="icon"><use href="#i-phone"/></svg>(+00) 555 0142 776</div>
    <div class="contact-line"><svg class="icon"><use href="#i-mail"/></svg>info@fernandgablerealty.com</div>
    <div class="contact-line"><svg class="icon"><use href="#i-pin"/></svg>27 Maple Row Eastfield, CT 06000</div>
    <div class="contact-line"><svg class="icon"><use href="#i-web"/></svg>www.fernandgablerealty.com</div>
  </div>
</section>

<!-- Envelope -->
<section class="sheet envelope">
  <svg class="shape-layer" viewBox="0 0 1040 500" preserveAspectRatio="none">
    <path d="M0 500 L0 480 L1040 290 L1040 310 L0 500 Z" fill="var(--navy)"/>
    <path d="M1012 292 L1040 276 L1040 288 Z" fill="var(--gold)"/>
  </svg>
  <div class="wordmark"><span class="mark-square"></span>Fern &amp; Gable Realty</div>
  <div class="contacts">
    <div class="contact-line"><svg class="icon"><use href="#i-pin"/></svg>27 Maple Row Eastfield, CT 06000</div>
    <div class="contact-line"><svg class="icon"><use href="#i-phone"/></svg>(+00) 555 0142 776</div>
    <div class="contact-line"><svg class="icon"><use href="#i-mail"/></svg>info@fernandgablerealty.com</div>
    <div class="contact-line"><svg class="icon"><use href="#i-web"/></svg>www.fernandgablerealty.com</div>
  </div>
  <div class="address-window"></div>
</section>

</body>
</html>
```